依頼詳細
販売商品は下記の3種類です。詳細はURLをご参照下さい。

1.工業用精製水 (用途:実験室などでの試験器具洗浄など)
http://www.hanabo-tenko.com/shop/goods/goods/goods.php?act=Goods&mode=Detail&id=00054986

2.バッテリー補充液 (用途:バッテリーの補充液など)
http://www.hanabo-tenko.com/shop/goods/goods/goods.php?act=Goods&mode=Detail&id=00054987

3.高純度精製水 (用途:エステスチーマーや加湿器の補給水など)
http://www.hanabo-tenko.com/shop/goods/goods/goods.php?act=Goods&mode=Detail&id=00066908

精製水は純度の高い水(きれいな水)ですので、商品に相応しい爽やかな印象を持っていただけるデザインを希望します。全体的にブルー系統のカラーを希望します。

添付の原案のレイアウト通りの必要はありません。見やすく目的に沿った内容であれば、画像等の追加、文章やフレーズ、フォント、文字サイズなどの修正、加筆もOKです。基本的にはデザインを重視したいと思います。

記載事項が多いので、A4サイズに収まるレイアウトの工夫をお願い致します。
記載項目
添付の【原案】をご参照下さい。
サイズ
A4
ページ数
両面
希望イメージ
シンプル 複雑
単色 カラフル
暗い 明るい
日常 高級
遊び心 厳粛
未来的 伝統的
女性的 男性的
希望する色
水色系
納品ファイル
• 高解像度JPG (.jpg)
• イラストレーター形式 (.ai)
補足説明

当社の要望・イメージに最も近いデザインでした。

みなさん非常に素晴らしいご提案でしたので、選定に苦慮いたしました。

選定できなかった皆様には申し訳ございませんでしたが、またの機会がございましたらよろしくお願い致します。皆様のご尽力にとても感謝致します。

この度は誠にありがとうございました。

```html
<!DOCTYPE html>
<html lang="ja">
<head>
<meta charset="utf-8">
<title>注文シート（FAX専用）</title>
<link rel="stylesheet" href="https://fonts.googleapis.com/css2?family=Noto+Sans+JP:wght@400;500;700;900&display=swap">
<style>
:root{
  --ink:#1d3a52;
  --bar:#1e8fd2;
  --bar-deep:#1574b3;
  --mid:#62b6e6;
  --line:#a8d3ee;
  --soft:#e7f5fd;
  --paper:#ffffff;
}
*{box-sizing:border-box;margin:0;padding:0}
html,body{width:871px;height:1200px;overflow:hidden;background:var(--paper)}
body{font-family:"Noto Sans JP",sans-serif;color:var(--ink);font-size:11px;position:relative}
.sheet{position:absolute;left:32px;top:26px;width:807px}
.header{display:flex;align-items:flex-end;justify-content:space-between;height:64px;border-bottom:3px solid var(--bar);padding-bottom:6px}
.send-dir{width:120px;height:54px;border:2px solid var(--bar);color:var(--bar-deep);display:flex;flex-direction:column;align-items:center;justify-content:center;font-size:10px;font-weight:700}
.send-dir svg{display:block;margin-bottom:2px}
.title{text-align:center}
.title h1{font-size:26px;font-weight:900;letter-spacing:2px;color:var(--bar-deep)}
.title p{font-size:10px;margin-top:2px}
.order-date{display:flex;align-items:center;background:var(--bar);color:#fff;height:30px;padding:0 10px;font-weight:700;font-size:12px;gap:8px}
.order-date span.blank{display:inline-block;width:44px;height:20px;background:#fff}
.section{margin-top:8px}
.sec-bar{display:flex;align-items:center;gap:12px;background:var(--bar);color:#fff;height:22px;padding:0 10px;font-weight:700;font-size:12.5px}
.sec-bar small{font-weight:400;font-size:9.5px}
.form-row{display:flex;border-bottom:1px solid var(--line);min-height:26px}
.form-row .cell{display:flex;align-items:center;border-right:1px solid var(--line)}
.form-row .cell:last-child{border-right:none}
.lbl{width:78px;display:flex;align-items:center;padding-left:8px;background:var(--soft);font-weight:500;font-size:10.5px;align-self:stretch}
.fill{flex:1;padding-left:6px;font-size:10px}
.box-row{display:flex;align-items:center;gap:16px;padding:6px 10px;border-bottom:1px solid var(--line);font-size:11px}
.chk{display:inline-flex;align-items:center;gap:4px}
.chk::before{content:"";width:11px;height:11px;border:1.5px solid var(--bar-deep);background:#fff;display:inline-block}
.pay-wrap{display:flex}
.pay-wrap .left{flex:1}
.request{width:260px;border-left:1px solid var(--line);padding:4px 8px;font-size:10px}
.request .req-title{display:inline-block;border:1px solid var(--bar-deep);color:var(--bar-deep);padding:0 6px;margin-bottom:4px;font-weight:700}
.request .chks{display:flex;gap:12px}
.products{display:flex;gap:10px;margin-top:6px}
.product{flex:1}
.product h3{background:var(--bar-deep);color:#fff;text-align:center;font-size:13.5px;font-weight:900;height:26px;line-height:26px;letter-spacing:1px}
.price{width:100%;border-collapse:collapse;font-size:10.5px}
.price th{background:var(--mid);color:#fff;font-weight:500;height:20px;font-size:10px}
.price td{border-bottom:1px solid var(--line);border-right:1px solid var(--line);height:22px;text-align:center}
.price td:last-child{border-right:none}
.price td.qty{background:var(--soft);font-weight:700}
.price td.yen{text-align:right;padding-right:6px}
.order-note{display:flex;justify-content:flex-end;align-items:center;gap:8px;margin-top:6px;font-size:10px}
.total-qty{display:flex;align-items:center;border:1.5px solid var(--bar-deep);height:24px}
.total-qty b{background:var(--bar-deep);color:#fff;height:100%;display:flex;align-items:center;padding:0 10px;font-size:11px}
.total-qty span{width:110px;text-align:right;padding-right:6px}
.ship-wrap{display:flex;gap:10px;margin-top:6px}
.ship-table{border-collapse:collapse;font-size:10.5px;width:390px}
.ship-table th{background:var(--mid);color:#fff;font-weight:500;height:20px}
.ship-table td{border-bottom:1px solid var(--line);border-right:1px solid var(--line);text-align:center;height:21px}
.ship-table td:last-child{border-right:none}
.ship-table td.area{background:var(--soft);font-weight:700}
.ship-side{flex:1;font-size:10.5px}
.ship-side .hint{font-size:9.5px;line-height:1.5;margin-bottom:6px}
.wish{border:1.5px solid var(--bar);padding:6px 8px}
.wish .date{display:flex;align-items:center;gap:6px;margin-bottom:6px;font-weight:700;color:var(--bar-deep)}
.wish .date i{display:inline-block;width:40px;border-bottom:1px solid var(--bar-deep);height:14px}
.times{display:grid;grid-template-columns:1fr 1fr;gap:5px 10px}
.sum-wrap{display:flex;gap:10px;margin-top:6px}
.sum-box{width:390px;border:1.5px solid var(--bar)}
.sum-box .head,.other .head{background:var(--bar);color:#fff;font-weight:700;padding:3px 8px;font-size:11px}
.sum-table{width:100%;border-collapse:collapse;font-size:10.5px}
.sum-table th{background:var(--soft);font-weight:500;height:22px;border-right:1px solid var(--line);border-bottom:1px solid var(--line)}
.sum-table td{height:34px;border-right:1px solid var(--line);text-align:right;padding-right:4px;vertical-align:bottom}
.sum-table th:last-child,.sum-table td:last-child{border-right:none}
.sum-box .foot{font-size:9px;padding:3px 8px;border-top:1px solid var(--line)}
.other{flex:1;border:1.5px solid var(--bar)}
.fax-band{position:absolute;left:32px;top:1110px;width:807px;height:58px;background:linear-gradient(90deg,var(--bar-deep),var(--bar) 60%,var(--mid));color:#fff;display:flex;align-items:center;justify-content:space-between;padding:0 18px}
.fax-band .num{font-size:42px;font-weight:900;letter-spacing:1px}
.fax-band .side{text-align:right;font-size:11px;line-height:1.5;font-weight:500}
</style>
</head>
<body>
<main class="sheet">
  <header class="header">
    <div class="send-dir">
      <svg width="28" height="22" viewBox="0 0 28 22"><path d="M14 1 L27 12 H19 V21 H9 V12 H1 Z" fill="none" stroke="#1574b3" stroke-width="2"/></svg>
      FAX 送信方向
    </div>
    <div class="title">
      <h1>注文シート（FAX専用）</h1>
      <p>本紙はお手数ですがコピーしてご利用下さい。</p>
    </div>
    <div class="order-date">ご注文日 <span class="blank"></span>月<span class="blank"></span>日</div>
  </header>

  <section class="section">
    <div class="sec-bar">ご注文者情報 <small>※ご記入いただいた情報は商品発送のためにのみ使用いたします。</small></div>
    <div class="form-row"><div class="cell" style="flex:1.4"><span class="lbl">フリガナ</span><span class="fill"></span></div><div class="cell" style="flex:1"><span class="lbl">ご担当者</span><span class="fill"></span></div></div>
    <div class="form-row" style="min-height:30px"><div class="cell" style="flex:1.4"><span class="lbl">お名前</span><span class="fill"></span></div><div class="cell" style="flex:1"><span class="lbl">ご担当者</span><span class="fill"></span></div></div>
    <div class="form-row" style="min-height:34px"><div class="cell" style="flex:1"><span class="lbl">ご住所</span><span class="fill">〒　　　－</span></div></div>
    <div class="form-row"><div class="cell" style="flex:1"><span class="lbl">電話番号</span><span class="fill"></span></div><div class="cell" style="flex:1"><span class="lbl">FAX番号</span><span class="fill"></span></div><div class="cell" style="flex:1"><span class="lbl">Eメール</span><span class="fill"></span></div></div>
  </section>

  <section class="section">
    <div class="sec-bar">お届け先情報 <small>※ご注文者と異なる場合のみご記入ください。</small></div>
    <div class="form-row"><div class="cell" style="flex:1.4"><span class="lbl">お名前</span><span class="fill"></span></div><div class="cell" style="flex:1"><span class="lbl">ご担当</span><span class="fill"></span></div></div>
    <div class="form-row" style="min-height:30px"><div class="cell" style="flex:1"><span class="lbl">ご住所</span><span class="fill">〒　　　－</span></div></div>
    <div class="form-row"><div class="cell" style="flex:1"><span class="lbl">電話番号</span><span class="fill"></span></div></div>
  </section>

  <section class="section">
    <div class="sec-bar">お支払い方法 <small>※いずれかにチェックを入れてください。</small></div>
    <div class="pay-wrap">
      <div class="left">
        <div class="box-row"><span class="chk">銀行振込</span><span class="chk">代金引換</span><span style="font-size:9.5px">※代金引換の場合は別途手数料がかかります。</span></div>
      </div>
      <div class="request"><span class="req-title">ご要望欄</span><div class="chks"><span class="chk">商品に同梱</span><span class="chk">別途郵送</span></div></div>
    </div>
  </section>

  <section class="section">
    <div class="sec-bar">伝票発行 <small>※必要な書類にチェックを入れてください。</small></div>
    <div class="box-row"><span class="chk">納品書</span><span class="chk">領収書</span><span class="chk">納品書と請求書</span><span>宛名：</span></div>
  </section>

  <section class="section">
    <div class="sec-bar">ご注文内容 <small>※ご希望の商品・数量をご記入ください。</small></div>
    <div class="products">
      <div class="product">
        <h3>工業用精製水 TSP－01</h3>
        <table class="price">
          <tr><th>まとめ買い</th><th>コック</th><th>単価(税込)</th><th>数量</th></tr>
          <tr><td class="qty" rowspan="2">1箱</td><td>あり</td><td class="yen">840円</td><td></td></tr>
          <tr><td>なし</td><td class="yen">896円</td><td></td></tr>
          <tr><td class="qty" rowspan="2">2箱</td><td>あり</td><td class="yen">1,620円</td><td></td></tr>
          <tr><td>なし</td><td class="yen">1,732円</td><td></td></tr>
          <tr><td class="qty" rowspan="2">5箱</td><td>あり</td><td class="yen">3,980円</td><td></td></tr>
          <tr><td>なし</td><td class="yen">4,260円</td><td></td></tr>
          <tr><td class="qty" rowspan="2">10箱以上</td><td>あり</td><td class="yen">8,540円</td><td></td></tr>
          <tr><td>なし</td><td class="yen">9,140円</td><td></td></tr>
          <tr><td class="qty" rowspan="2">20箱以上</td><td>あり</td><td class="yen">16,600円</td><td></td></tr>
          <tr><td>なし</td><td class="yen">17,640円</td><td></td></tr>
        </table>
      </div>
      <div class="product">
        <h3>バッテリー補充液 TSP－02</h3>
        <table class="price">
          <tr><th>まとめ買い</th><th>コック</th><th>単価(税込)</th><th>数量</th></tr>
          <tr><td class="qty" rowspan="2">1箱</td><td>あり</td><td class="yen">840円</td><td></td></tr>
          <tr><td>なし</td><td class="yen">896円</td><td></td></tr>
          <tr><td class="qty" rowspan="2">2箱</td><td>あり</td><td class="yen">1,620円</td><td></td></tr>
          <tr><td>なし</td><td class="yen">1,732円</td><td></td></tr>
          <tr><td class="qty" rowspan="2">5箱</td><td>あり</td><td class="yen">3,980円</td><td></td></tr>
          <tr><td>なし</td><td class="yen">4,260円</td><td></td></tr>
          <tr><td class="qty" rowspan="2">10箱以上</td><td>あり</td><td class="yen">8,540円</td><td></td></tr>
          <tr><td>なし</td><td class="yen">9,140円</td><td></td></tr>
          <tr><td class="qty" rowspan="2">20箱以上</td><td>あり</td><td class="yen">16,600円</td><td></td></tr>
          <tr><td>なし</td><td class="yen">17,640円</td><td></td></tr>
        </table>
      </div>
      <div class="product">
        <h3>高純度精製水 TSP－03</h3>
        <table class="price">
          <tr><th>まとめ買い</th><th>コック</th><th>単価(税込)</th><th>数量</th></tr>
          <tr><td class="qty" rowspan="2">1箱</td><td>あり</td><td class="yen">1,050円</td><td></td></tr>
          <tr><td>なし</td><td class="yen">1,106円</td><td></td></tr>
          <tr><td class="qty" rowspan="2">2箱</td><td>あり</td><td class="yen">2,040円</td><td></td></tr>
          <tr><td>なし</td><td class="yen">2,152円</td><td></td></tr>
          <tr><td class="qty" rowspan="2">5箱</td><td>あり</td><td class="yen">4,980円</td><td></td></tr>
          <tr><td>なし</td><td class="yen">5,260円</td><td></td></tr>
          <tr><td class="qty" rowspan="2">10箱以上</td><td>あり</td><td class="yen">9,720円</td><td></td></tr>
          <tr><td>なし</td><td class="yen">10,280円</td><td></td></tr>
          <tr><td class="qty" rowspan="2">20箱以上</td><td>あり</td><td class="yen">18,900円</td><td></td></tr>
          <tr><td>なし</td><td class="yen">20,020円</td><td></td></tr>
        </table>
      </div>
    </div>
    <div class="order-note"><span>※1箱は10リットル入りです。コック付きは別途料金となります。</span><div class="total-qty"><b>合計数量</b><span>箱</span></div></div>
  </section>

  <section class="section">
    <div class="sec-bar">送料及び配送日数について <small>※地域により異なります。</small></div>
    <div class="ship-wrap">
      <table class="ship-table">
        <tr><th>地域</th><th>送料</th><th>日数</th><th>地域</th><th>送料</th><th>日数</th></tr>
        <tr><td class="area">北海道</td><td>840円</td><td>2日</td><td class="area">中国</td><td>525円</td><td>1日</td></tr>
        <tr><td class="area">東北</td><td>630円</td><td>1日</td><td class="area">四国</td><td>525円</td><td>1日</td></tr>
        <tr><td class="area">関東</td><td>525円</td><td>1日</td><td class="area">九州</td><td>630円</td><td>1日</td></tr>
        <tr><td class="area">中部</td><td>525円</td><td>1日</td><td class="area">沖縄</td><td>1,260円</td><td>3日</td></tr>
        <tr><td class="area">近畿</td><td>525円</td><td>1日</td><td class="area">離島</td><td>別途</td><td>—</td></tr>
      </table>
      <div class="ship-side">
        <p class="hint">※10箱以上のご注文は送料無料となります。<br>※配送日数は目安です。ご了承ください。</p>
        <div class="wish">
          <div class="date">お届け希望日 <i></i>月<i></i>日</div>
          <div class="times">
            <span class="chk">午前中</span><span class="chk">12～14時</span>
            <span class="chk">14～16時</span><span class="chk">16～18時</span>
            <span class="chk">18～20時</span><span class="chk">20～21時</span>
          </div>
        </div>
      </div>
    </div>
  </section>

  <section class="sum-wrap">
    <div class="sum-box">
      <div class="head">お支払いの合計金額をご確認されたい場合にご記入ください。</div>
      <table class="sum-table">
        <tr><th>商品代金合計</th><th>送料</th><th>代引手数料</th><th>お支払総額</th></tr>
        <tr><td>円</td><td>円</td><td>円</td><td>円</td></tr>
      </table>
      <div class="foot">※折り返しご注文内容確認のご連絡をいたします。</div>
    </div>
    <div class="other">
      <div class="head">その他のご要望がございましたらご記入ください。</div>
    </div>
  </section>
</main>

<footer class="fax-band">
  <div class="num">FAX:0120-345-678</div>
  <div class="side">FAX 専用受付<br>ご注文内容を再度ご確認ください</div>
</footer>
</body>
</html>
```